Business Card Design

We need a business card for our company that says "Thank You for purchasing our product". We sell all sorts of products online through the Zelvora fulfilment by Zelvora.example. This is just our way of communicating a thank you. Colors we would like to see are Black, White Silver Royal Blue, Hunter Green. One of our favorite photographers is Marten Holloway. He used nice clean designs on his prints.

http://www.lookfinder.example/url?sa=i&rct=j&q=&esrc=s&source=images&cd=&cad=rja&uact=8&ved=0CAcQjRw&url=http%3A%2F%2Fwww.brightgallery.example%2Fexplore%2Fcollection%2Fartwork%2F20417&ei=oSvCVPzyPIe5ggT_noOYCQ&bvm=bv.84349003,d.eXY&psig=AFQjCNG6t4yNl0gAwObRW3BfypWv3eXIMQ&ust=1422097697203334

Industry/Entity Type

Business

Contact Information for Business Card

Pete Harrow
Harrow Ventures, llc
4379 South East Ninth Lane
Gainesville, Florida 32791

```html
<!DOCTYPE html>
<html lang="en">
<head>
<meta charset="UTF-8">
<title>Harrow Ventures – Thank You Business Card</title>
<link href="https://fonts.googleapis.com/css2?family=Montserrat:wght@400;600&family=Parisienne&display=swap" rel="stylesheet">
<style>
  :root {
    --page-bg: #e6e4e1;
    --card-white: #fbfbfb;
    --silver-light: #e9e9ec;
    --silver-mid: #b9b8bd;
    --silver-dark: #7c7b80;
    --photo-light: #b8b8b8;
    --photo-dark: #2a2a2a;
    --ink: #1c1c1c;
    --ink-soft: #3a3a3a;
    --band: #d6d6d8;
  }
  * { margin: 0; padding: 0; box-sizing: border-box; }
  html, body { width: 1200px; height: 900px; overflow: hidden; }
  body {
    background: var(--page-bg);
    position: relative;
    font-family: "Montserrat", Arial, sans-serif;
  }
  .card {
    position: absolute;
    left: 285px;
    width: 630px;
    height: 360px;
    box-shadow: 0 6px 18px rgba(0,0,0,0.25);
    overflow: hidden;
  }
  .card-back { top: 60px; }
  .card-front { top: 480px; background: var(--card-white); }
  .card svg { display: block; width: 100%; height: 100%; }
  .thanks-line {
    font-family: "Parisienne", cursive;
    font-size: 36px;
    fill: var(--ink-soft);
  }
  .holder-name {
    position: absolute;
    left: 400px;
    top: 92px;
    font-weight: 600;
    font-size: 24px;
    color: var(--ink);
  }
  .company-block {
    position: absolute;
    left: 40px;
    top: 245px;
    width: 310px;
    text-align: right;
  }
  .company-name {
    font-weight: 600;
    font-size: 22px;
    color: var(--ink-soft);
    text-align: left;
  }
  .company-address {
    margin-top: 10px;
    font-size: 11px;
    line-height: 1.4;
    color: var(--ink-soft);
  }
</style>
</head>
<body>

  <section class="card card-back">
    <svg viewBox="0 0 630 360" xmlns="http://www.w3.org/2000/svg">
      <defs>
        <linearGradient id="photoTone" x1="0" y1="0" x2="1" y2="1">
          <stop offset="0" stop-color="var(--photo-dark)"/>
          <stop offset="0.5" stop-color="var(--photo-light)"/>
          <stop offset="1" stop-color="var(--photo-dark)"/>
        </linearGradient>
        <linearGradient id="bandTone" x1="0" y1="0" x2="0" y2="1">
          <stop offset="0" stop-color="#f2f2f4"/>
          <stop offset="1" stop-color="var(--silver-mid)"/>
        </linearGradient>
      </defs>
      <rect class="landscape-photo" width="630" height="360" fill="url(#photoTone)"
            role="img" aria-label="Black and white photograph of a forest waterfall flowing over rocks"/>
      <polygon class="silver-band" points="0,262 630,72 630,150 0,360" fill="url(#bandTone)"/>
      <text class="thanks-line" transform="translate(30 318) rotate(-16.8)">Thank You for purchasing our product</text>
    </svg>
  </section>

  <section class="card card-front">
    <svg viewBox="0 0 630 360" xmlns="http://www.w3.org/2000/svg" aria-hidden="true">
      <defs>
        <linearGradient id="whiteTone" x1="0" y1="0" x2="1" y2="1">
          <stop offset="0" stop-color="#ffffff"/>
          <stop offset="1" stop-color="#dcdcde"/>
        </linearGradient>
        <linearGradient id="metalTone" x1="0" y1="0" x2="0.3" y2="1">
          <stop offset="0" stop-color="var(--silver-dark)"/>
          <stop offset="0.35" stop-color="var(--silver-light)"/>
          <stop offset="0.55" stop-color="#fdfdfd"/>
          <stop offset="1" stop-color="var(--silver-dark)"/>
        </linearGradient>
      </defs>
      <rect width="630" height="360" fill="url(#whiteTone)"/>
      <polygon class="metal-panel" points="220,0 630,0 630,360 400,360" fill="url(#metalTone)"/>
    </svg>
    <div class="holder-name">Pete Harrow</div>
    <div class="company-block">
      <div class="company-name">Harrow Ventures LLC</div>
      <div class="company-address">4379 South East Ninth Lane Gainesville,<br>Florida 32791</div>
    </div>
  </section>

</body>
</html>
```